Etiketten für Nahrungsergänzung für Tiere
Zielgruppe
Wir stellen kolloidale Mischungen für Tiere her. Dies sind grob gesagt Nahrungsmittelergänzungen. Die Zielgruppe sind Tierbesitzer bzw. gesundheitsbewusste Menschen.
Aufgabenstellung
natürlich, in braun, beige, gold oder hellblau Tönen. Das Etikett wird auf eine Flasche aufgebraucht in der sich eine Flüssigkeit befindet. Das Etikett ist breiter als hoch. 115 x 61 mm (B x H)
Bisher haben wir blaue Flaschen verwendet und waren dadurch mit der Farbgebung ehr kühl und reduziert. In Zukunft wollen wir braune Flaschen mit schwarzen Deckel verwendet. Damit darf die Farbgebung auch wärmer, natürlich und das Etikett auch mit mehr Details versehen werden.
In den Uploads füge ich das aktuell Logo hinzu. Dies verwenden wir in braun/gold und in grün. Falls sich diese Gestaltung nicht so günstig auswirkt, haben wir ein 'alternative' Logo hinzugefügt. Da die Seite nächstes Jahr komplett überarbeitet wird und unsere Firma sich vergrößert, kann diese Änderung durchgeführt werden.
Ich lade noch ein Etikett hoch, welches wir für die Einzelelemente nutzen. Hier sind und bleiben die Flaschen nach wir vor blau (Herstellervorgaben), dadurch sind die Etikett sehr kühl und reduziert. Das darf auf den Entwurf für die Mischungen sehr gern deutlich verändert werden :-)

```html
<!DOCTYPE html>
<html lang="de">
<head>
<meta charset="utf-8">
<title>Etiketten Kolloide</title>
<link rel="stylesheet" href="https://fonts.googleapis.com/css2?family=Manrope:wght@400;500;700;800&display=swap">
<style>
  :root {
    --page: #ffffff;
    --cream: #f7f5dd;
    --ink: #2b2b2b;
    --white: #ffffff;
    --titan-main: #5c4033;
    --titan-accent: #a77b5a;
    --silizium-main: #569dd6;
    --silizium-accent: #a8dbe0;
  }
  html, body {
    margin: 0;
    width: 1200px;
    height: 1199px;
    overflow: hidden;
    background: var(--page);
    font-family: "Manrope", Arial, sans-serif;
    color: var(--ink);
  }
  .sheet { position: relative; width: 1200px; height: 1199px; }

  .label {
    position: absolute;
    left: 232px;
    width: 738px;
    height: 392px;
    filter: drop-shadow(12px 14px 8px rgba(0,0,0,0.35));
  }
  .label--titan { top: 162px; --main: var(--titan-main); --accent: var(--titan-accent); --band-text: var(--white); }
  .label--silizium { top: 646px; --main: var(--silizium-main); --accent: var(--silizium-accent); --band-text: var(--ink); }

  .label__shapes { position: absolute; inset: 0; width: 738px; height: 392px; }
  .shape-main { fill: var(--main); }
  .shape-accent { fill: var(--accent); }
  .shape-cream { fill: var(--cream); }
  .brand-mark { fill: none; stroke: var(--accent); stroke-width: 4; }

  .label__title {
    position: absolute;
    left: 56px;
    top: 230px;
    margin: 0;
    font-size: 31px;
    font-weight: 400;
    letter-spacing: 0.5px;
    color: var(--ink);
    line-height: 1;
  }
  .label--titan .label__title { color: var(--white); }
  .label__title strong { font-weight: 800; }

  .label__ingredients {
    position: absolute;
    left: 56px;
    top: 288px;
    margin: 0;
    font-size: 13px;
    line-height: 17px;
    color: var(--band-text);
  }
  .label__ingredients strong { font-weight: 700; }

  .sizes {
    position: absolute;
    top: 358px;
    left: 56px;
    margin: 0; padding: 0;
    list-style: none;
    display: flex;
    font-size: 10.5px;
    color: var(--white);
  }
  .sizes li { display: flex; align-items: center; }
  .sizes li + li { margin-left: 0; }
  .sizes .box {
    width: 11px; height: 11px;
    background: var(--cream);
    margin-right: 7px;
  }
  .sizes li:nth-child(1) { width: 72px; }
  .sizes li:nth-child(2) { width: 72px; }
  .sizes li:nth-child(3) { width: 75px; }

  .label__info {
    position: absolute;
    left: 427px;
    width: 290px;
    font-size: 10.6px;
    line-height: 15.5px;
  }
  .label__process { top: 88px; margin: 0; font-weight: 700; font-size: 12.4px; line-height: 17px; }
  .label__notes { top: 196px; margin: 0; text-align: justify; }
  .label__maker { top: 284px; margin: 0; font-weight: 700; font-size: 12.4px; line-height: 16.5px; }
  .label__batch {
    position: absolute;
    left: 427px;
    top: 358px;
    margin: 0;
    font-size: 11.5px;
    color: var(--white);
  }
</style>
</head>
<body>
<main class="sheet">

  <article class="label label--titan">
    <svg class="label__shapes" viewBox="0 0 738 392" aria-hidden="true">
      <rect class="shape-cream" x="0" y="0" width="738" height="392"/>
      <polygon class="shape-main" points="0,0 308,0 386,392 0,392"/>
      <polygon class="shape-accent" points="308,0 324,0 402,392 386,392"/>
      <polygon class="shape-main" points="392,354 738,354 738,378 396,378"/>
      <polygon class="shape-cream" points="330,354 392,354 396,378 335,378" opacity="0"/>
      <polygon class="shape-accent" points="0,280 357,280 350,323 0,323"/>
      <circle class="brand-mark" cx="120" cy="118" r="52"/>
    </svg>
    <h2 class="label__title">PURIS <strong>TITAN</strong></h2>
    <p class="label__ingredients">Kolloid in wässriger Lösung<br><strong>Inhaltsstoffe:</strong> 99,9% reines Titan in Bidestillat</p>
    <ul class="sizes">
      <li><span class="box"></span>30 ml</li>
      <li><span class="box"></span>50 ml</li>
      <li><span class="box"></span>100 ml</li>
      <li><span class="box"></span>200 ml</li>
    </ul>
    <p class="label__info label__process">Kolloid aus Protonenresonanzverfahren<br>50 ppm bei Herstellung in doppelt<br>destilliertem Wasser</p>
    <p class="label__info label__notes">Bei Raumtemperatur und lichtgeschützt lagern. Vor Mikrowellen und magnetischen Feldern fernhalten. PPM-Messmethode: Atomspektralanalyse. Anwendung nach dem Quatenprinzip der verschränkten Teilchen. Nicht für den menschlichen Verzehr geeignet.</p>
    <p class="label__info label__maker">Naturquelle, Am Lindenweg 8, 99441<br>Kranichfeld</p>
    <p class="label__batch">MHD=Chargen-Nr:</p>
  </article>

  <article class="label label--silizium">
    <svg class="label__shapes" viewBox="0 0 738 392" aria-hidden="true">
      <rect class="shape-cream" x="0" y="0" width="738" height="392"/>
      <polygon class="shape-main" points="0,0 308,0 386,392 0,392"/>
      <polygon class="shape-accent" points="308,0 324,0 402,392 386,392"/>
      <polygon class="shape-main" points="392,354 738,354 738,378 396,378"/>
      <polygon class="shape-accent" points="0,280 357,280 350,323 0,323"/>
      <circle class="brand-mark" cx="120" cy="118" r="52" style="stroke: var(--cream)"/>
    </svg>
    <h2 class="label__title">PURIS <strong>SILIZIUM</strong></h2>
    <p class="label__ingredients">Kolloid in wässriger Lösung<br><strong>Inhaltsstoffe:</strong> 99,999% reines Titan in Bidestillat</p>
    <ul class="sizes">
      <li><span class="box"></span>30 ml</li>
      <li><span class="box"></span>50 ml</li>
      <li><span class="box"></span>100 ml</li>
      <li><span class="box"></span>200 ml</li>
    </ul>
    <p class="label__info label__process">Kolloid aus Protonenresonanzverfahren<br>55 ppm bei Herstellung in doppelt<br>destilliertem Wasser</p>
    <p class="label__info label__notes">Bei Raumtemperatur und lichtgeschützt lagern. Vor Mikrowellen und magnetischen Feldern fernhalten. PPM-Messmethode: Atomspektralanalyse. Anwendung nach dem Quatenprinzip der verschränkten Teilchen. Nicht für den menschlichen Verzehr geeignet.</p>
    <p class="label__info label__maker">Marlene Vogt, Am Lindenweg 8, 99441<br>Kranichfeld</p>
    <p class="label__batch">MHD=Chargen-Nr:</p>
  </article>

</main>
</body>
</html>
```